Car rental website design for a UAE car rental company

This project is about creating a new website design for a car rental company located in Dubai (United Arab Emirates), I opened the same project a few months ago but I didn't receive a lot of appealing entries so I closed it but this time I am marking the project as guaranteed to avoid such situation again, if you have already provided a design before then please re-submit again on this project so that it is considered while reviewing all the designs

A few important things:

1- We need a simple non-complex design
2- The final deliverable would be 2 screens (PSD, JPEG ... etc), the first screen is for the home page and the second screen is for an internal page
3- The home page must have a section that end users can use to rent a car online directly from the home page instead of going into some inner pages
4- The current website is very old and not very appealing so avoid creating a similar design (www.quarvin-drive.example)
5- The name is Quarvin but the company rents normal cars (no Limousin cars will be rented) so avoid adding any fancy cars in the images/graphics used in the design, just normal end users cars
6- The expected pages would be: home, About us, Our team, Strategy, Contact us and links to social media pages
7- The attachments include the company's logo and some screens from other car rental companies that provide online rentals/payments

If you have any questions please feel free to ask and please note that we will need the designs urgently

Thanks

Target Market(s)

Dubai - United Arab Emirates

Industry/Entity Type

It Company

Number of Pages Required

2 page

Font styles to use
Sans Serif

Requirements
Must have
• Check the project details
Nice to have
Should not have

```html
<!DOCTYPE html>
<html lang="en">
<head>
<meta charset="utf-8">
<title>Quarvin Rent A Car</title>
<link rel="stylesheet" href="https://fonts.googleapis.com/css2?family=Source+Sans+3:wght@300;400;600;700&display=swap">
<style>
:root{
  --crimson:#a1093b;
  --crimson-dark:#8a0632;
  --ink:#1c1c1c;
  --navy:#10123a;
  --text:#666;
  --footer:#222;
  --orange:#f7760f;
  --orange-light:#ff9a26;
  --white:#fff;
}
*{margin:0;padding:0;box-sizing:border-box}
html,body{width:1200px;height:843px;overflow:hidden}
body{font-family:"Source Sans 3",sans-serif;background:var(--white);position:relative;color:var(--text)}
.topbar{position:absolute;left:0;top:0;width:1200px;height:69px;background:linear-gradient(#fff,#e4e4e4)}
.call{position:absolute;right:162px;top:11px;text-align:right}
.call-label{font-size:14px;line-height:14px;font-weight:600;color:#999;letter-spacing:.3px}
.call-number{font-size:27px;line-height:26px;font-weight:600;color:var(--ink)}
.call-icon{position:absolute;left:-40px;top:13px}
.navbar{position:absolute;left:0;top:69px;width:1200px;height:44px;background:var(--crimson);border-bottom:2px solid #c9c9c9}
.nav{position:absolute;left:368px;top:0;display:flex;height:42px;list-style:none}
.nav li{display:flex;align-items:center;padding:0 17px;color:var(--white);font-weight:600;font-size:14px;border-left:1px solid rgba(255,255,255,.2)}
.nav li.home{background:var(--crimson-dark);padding:0 13px}
.search{position:absolute;left:805px;top:6px;width:234px;height:30px;background:var(--white);border-radius:4px;font-size:11px;font-style:italic;color:#444;padding:9px 8px}
.search svg{position:absolute;right:8px;top:8px}
.logo{position:absolute;left:161px;top:0;width:150px;height:141px;z-index:5;filter:drop-shadow(0 2px 3px rgba(0,0,0,.3))}
.logo-card{position:absolute;inset:0;background:var(--white);clip-path:polygon(0 0,100% 0,100% 100%,0 82%)}
.logo-mark{position:absolute;left:52px;top:14px;width:46px;height:46px;background:var(--crimson)}
.logo-name{position:absolute;left:0;width:150px;top:68px;text-align:center;font-size:25px;font-weight:600;color:var(--crimson);line-height:1}
.hero{position:absolute;left:0;top:113px;width:1200px;height:538px;background:linear-gradient(#4f6380 0%,#9aa2a8 30%,#c7a77c 52%,#6b5a48 68%,#b59a7c 85%,#8d7459 100%)}
.hero-line{position:absolute;left:0;top:651px;width:1200px;height:5px;background:var(--crimson)}
.tagline{position:absolute;left:274px;top:415px;width:531px;height:107px;background:rgba(235,235,235,.88);border:1px solid var(--white);outline:1px solid rgba(255,255,255,.7);outline-offset:-4px;padding:10px 16px}
.tagline-main{font-size:46px;font-weight:300;color:var(--crimson);line-height:1.05;white-space:nowrap}
.tagline-main b{font-weight:700;color:#000}
.tagline-sub{font-size:21px;color:#222;margin-top:3px}
.booking{position:absolute;left:809px;top:204px;width:230px;height:452px;background:var(--crimson)}
.booking-head{height:110px;background:var(--ink);clip-path:polygon(0 0,100% 0,100% 100%,0 88%);padding:18px 17px;color:var(--white);border-radius:3px 3px 0 0}
.booking-head small{display:block;font-size:21px;font-weight:300;line-height:1}
.booking-head strong{display:block;font-size:35px;font-weight:600;line-height:1.05;margin-top:2px}
.booking-form{position:absolute;left:14px;top:112px;width:201px}
.field-label{font-size:11.5px;line-height:14px;height:14px;font-weight:600;color:var(--white);margin-bottom:6px;white-space:nowrap}
.field{height:29px;background:var(--white);border-radius:3px;font-size:10px;line-height:13px;color:#444;padding:8px 11px;position:relative;margin-bottom:9px}
.field svg{position:absolute;right:7px;top:7px}
.field-row{display:flex;gap:8px}
.field-row .date{width:126px}
.field-row .time{width:66px}
.quote{height:30px;margin-top:15px;background:linear-gradient(var(--orange-light),var(--orange));color:var(--white);font-weight:600;font-size:13px;text-align:center;line-height:30px;border-radius:2px}
.field-row:last-of-type + .quote{margin-top:6px}
.welcome{position:absolute;left:162px;top:675px;width:880px}
.welcome h1{font-size:22px;line-height:26px;font-weight:600;color:var(--navy)}
.welcome p{font-size:12px;line-height:18px;margin-top:11px}
.welcome p+p{margin-top:18px}
.footer{position:absolute;left:0;top:798px;width:1200px;height:45px;background:var(--footer)}
.copyright{position:absolute;left:162px;top:14px;font-size:12px;color:#999}
.social{position:absolute;right:161px;top:7px;display:flex;gap:8px}
.social span{width:30px;height:30px;border-radius:50%;background:#555}
.social span:first-child{background:var(--white)}
</style>
</head>
<body>
<header>
  <div class="topbar">
    <div class="call">
      <svg class="call-icon" width="26" height="26" viewBox="0 0 24 24"><path fill="#999" d="M6.6 10.8a15 15 0 0 0 6.6 6.6l2.2-2.2c.3-.3.7-.4 1-.2 1.1.4 2.3.6 3.6.6.6 0 1 .4 1 1V20c0 .6-.4 1-1 1A17 17 0 0 1 3 4c0-.6.4-1 1-1h3.5c.6 0 1 .4 1 1 0 1.3.2 2.5.6 3.6.1.3 0 .7-.2 1z"/></svg>
      <div class="call-label">FREE CALL</div>
      <div class="call-number">+971 400 12345</div>
    </div>
  </div>
  <div class="logo">
    <div class="logo-card"></div>
    <div class="logo-mark"></div>
    <div class="logo-name">Quarvin</div>
  </div>
  <nav class="navbar">
    <ul class="nav">
      <li class="home"><svg width="20" height="18" viewBox="0 0 20 18"><path fill="#fff" d="M10 1 1 9h3v8h4v-5h4v5h4V9h3z"/></svg></li>
      <li>ABOUT US</li>
      <li>OUR TEAM</li>
      <li>STRATEGY</li>
      <li>CONTACT US</li>
    </ul>
    <div class="search">Search...
      <svg width="13" height="13" viewBox="0 0 13 13"><circle cx="5" cy="5" r="4" fill="none" stroke="#aaa" stroke-width="1.5"/><path d="M8 8l4 4" stroke="#aaa" stroke-width="1.5"/></svg>
    </div>
  </nav>
</header>

<section class="hero" role="img" aria-label="Photo of a white family SUV parked on desert sand in front of the Dubai skyline at sunset"></section>
<div class="hero-line"></div>

<div class="tagline">
  <div class="tagline-main">Experience an <b>Extra Mile</b></div>
  <div class="tagline-sub">Of Comfort, Pleasure and leisure Form The Best</div>
</div>

<aside class="booking">
  <div class="booking-head"><small>BOOK A</small><strong>RENTAL CAR</strong></div>
  <div class="booking-form">
    <div class="field-label">Pick Up Location</div>
    <div class="field">Select<svg width="12" height="16" viewBox="0 0 12 16"><path fill="#888" d="M6 1l5 6H1zM6 15l5-6H1z"/></svg></div>
    <div class="field-label">Return Location</div>
    <div class="field">Select<svg width="12" height="16" viewBox="0 0 12 16"><path fill="#888" d="M6 1l5 6H1zM6 15l5-6H1z"/></svg></div>
    <div class="field-label">Vehicle Type (Group)</div>
    <div class="field">Show All Vehicles<svg width="12" height="16" viewBox="0 0 12 16"><path fill="#888" d="M6 1l5 6H1zM6 15l5-6H1z"/></svg></div>
    <div class="field-label">Pick-Up Date &amp; Time</div>
    <div class="field-row">
      <div class="field date">Select<svg width="15" height="15" viewBox="0 0 15 15"><rect x="1" y="2" width="13" height="12" fill="none" stroke="#888"/><path d="M1 5h13M4 8h2M8 8h2M4 11h2M8 11h2" stroke="#888"/></svg></div>
      <div class="field time">16:00<svg width="12" height="16" viewBox="0 0 12 16"><path fill="#888" d="M6 1l5 6H1zM6 15l5-6H1z"/></svg></div>
    </div>
    <div class="field-label">Return Date &amp; Time</div>
    <div class="field-row">
      <div class="field date">Select<svg width="15" height="15" viewBox="0 0 15 15"><rect x="1" y="2" width="13" height="12" fill="none" stroke="#888"/><path d="M1 5h13M4 8h2M8 8h2M4 11h2M8 11h2" stroke="#888"/></svg></div>
      <div class="field time">16:00<svg width="12" height="16" viewBox="0 0 12 16"><path fill="#888" d="M6 1l5 6H1zM6 15l5-6H1z"/></svg></div>
    </div>
    <div class="quote">GET A FREE QUOTE</div>
  </div>
</aside>

<main class="welcome">
  <h1>WELCOME TO QUARVIN</h1>
  <p>As Dubai is expected to welcome millions of tourists and visitors, car rental industry is believed to escalate more rapidly in the region.</p>
  <p>Over the past five years, demands for car rentals in Dubai has been augmenting at a healthy pace and is currently registering a growth rate of 20 to 25 percent per year. The swift economic growth and the number.....</p>
</main>

<footer class="footer">
  <div class="copyright">©Copyright 2015, Quarvin. All rights reserved</div>
  <div class="social"><span></span><span></span><span></span></div>
</footer>
</body>
</html>
```